Letterhead and Envelopes design using existing logo. Logo can be found at ridgemontcaldera.example

Use existing logo (attached) and incorporate in letterhead and envelope designs.

Current logo can be viewed at ridgemontcaldera.example the web site reflect various parent and sub companies. Please see attached as well.

Target Market(s)

Other oil and gas operators.

Industry/Entity Type

Oil And Gas

Font styles to use
Sans Serif

Colors

Designer to choose colors to be used in the design.

Requirements
Must have
• Current logo and address
Nice to have
• Modern, contemporary approach yet incorporate existing traditional design.
• After design is selected for Ridgemont Caldera Holdings I will use similar design for Royalties, Exploration, Energy and Farms with different color schemes.

```html
<!DOCTYPE html>
<html lang="en">
<head>
<meta charset="utf-8">
<title>Ridgemont Caldera Holdings — Letterhead</title>
<link rel="stylesheet" href="https://fonts.googleapis.com/css2?family=Open+Sans:wght@400;600&display=swap">
<style>
  :root {
    --backdrop: #e6e6e6;
    --paper: #ffffff;
    --ink: #333333;
    --ink-strong: #2b2b2b;
    --rule: #6f6f6f;
    --accent-green: #6a9a3c;
  }
  * { margin: 0; padding: 0; box-sizing: border-box; }
  html, body {
    width: 1200px;
    height: 1200px;
    overflow: hidden;
    background: var(--backdrop);
    font-family: "Open Sans", Arial, sans-serif;
  }
  .letterhead {
    position: absolute;
    left: 183px;
    top: 40px;
    width: 834px;
    height: 1120px;
    background: var(--paper);
  }
  .brand {
    position: absolute;
    left: 54px;
    top: 105px;
    display: flex;
    align-items: center;
    gap: 14px;
  }
  .brand-dot {
    width: 80px;
    height: 80px;
    border-radius: 50%;
    background: var(--accent-green);
    flex: none;
  }
  .brand-name {
    font-size: 17px;
    font-weight: 600;
    line-height: 1.2;
    color: var(--ink-strong);
    width: 150px;
  }
  .contact-block {
    position: absolute;
    left: 558px;
    top: 95px;
    height: 99px;
    border-left: 1.5px solid var(--rule);
    padding-left: 19px;
    color: var(--ink);
    font-size: 13px;
    line-height: 16px;
    font-style: normal;
  }
  .company {
    font-weight: 600;
    color: var(--ink-strong);
    margin-top: -1px;
  }
  .address { margin-bottom: 6px; }
  .contact-line {
    display: flex;
    align-items: center;
    gap: 6px;
  }
  .contact-line svg {
    width: 11px;
    height: 11px;
    flex: none;
    fill: var(--accent-green);
  }
</style>
</head>
<body>
  <main class="letterhead">
    <div class="brand">
      <span class="brand-dot"></span>
      <span class="brand-name">Ridgemont Caldera Holdings</span>
    </div>

    <address class="contact-block">
      <div class="company">Ridgemont Caldera Holdings, LLC.</div>
      <div class="address">PO Box 418 Lakemont,<br>North Dakota 58990</div>
      <div class="contact-line">
        <svg viewBox="0 0 24 24" aria-hidden="true"><path d="M6.6 10.8a15.1 15.1 0 0 0 6.6 6.6l2.2-2.2a1 1 0 0 1 1-.25 11.4 11.4 0 0 0 3.6.57 1 1 0 0 1 1 1V20a1 1 0 0 1-1 1A17 17 0 0 1 3 4a1 1 0 0 1 1-1h3.5a1 1 0 0 1 1 1c0 1.25.2 2.45.57 3.57a1 1 0 0 1-.25 1z"/></svg>
        <span>(555) 310.4821</span>
      </div>
      <div class="contact-line">
        <svg viewBox="0 0 24 24" aria-hidden="true"><path d="M2 5h20v14H2z M3.5 6.5 12 12.5l8.5-6"/></svg>
        <span>reception@ridgemontcaldera.example</span>
      </div>
      <div class="contact-line">
        <svg viewBox="0 0 24 24" aria-hidden="true"><path d="M12 2a10 10 0 1 0 0 20 10 10 0 0 0 0-20zm6.9 6h-3a15.7 15.7 0 0 0-1.4-3.6A8 8 0 0 1 18.9 8zM12 4c.8 1.2 1.5 2.5 1.9 4h-3.8c.4-1.5 1.1-2.8 1.9-4zM4.3 14a8.2 8.2 0 0 1 0-4h3.4a16.5 16.5 0 0 0 0 4zm.8 2h3a15.7 15.7 0 0 0 1.4 3.6A8 8 0 0 1 5.1 16zm3-8h-3a8 8 0 0 1 4.4-3.6A15.7 15.7 0 0 0 8.1 8zM12 20c-.8-1.2-1.5-2.5-1.9-4h3.8c-.4 1.5-1.1 2.8-1.9 4zm2.3-6H9.7a14.7 14.7 0 0 1 0-4h4.6a14.7 14.7 0 0 1 0 4zm.3 5.6a15.7 15.7 0 0 0 1.4-3.6h3a8 8 0 0 1-4.4 3.6zM16.3 14a16.5 16.5 0 0 0 0-4h3.4a8.2 8.2 0 0 1 0 4z"/></svg>
        <span>www.ridgemontcaldera.example</span>
      </div>
    </address>
  </main>
</body>
</html>
```